Business card design needed

I need a business card for my Sydney Painting Business, that specialises in painting High -end residential homes. i want the design to look clean, modern and edgy. i also want a logo next to the RK Decorating, using RKD together.

Industry/Entity Type

Residential

Contact Information for Business Card

RK Decorating (business name),LIC 581062B, Rob Kellaway, robert.kellaway@fernmail.net, mobile 0412573068

```html
<!DOCTYPE html>
<html lang="en">
<head>
<meta charset="utf-8">
<title>RK Decorating – Business Card</title>
<link rel="stylesheet" href="https://fonts.googleapis.com/css2?family=Michroma&family=Archivo:wght@400&display=swap">
<style>
  :root {
    --page-bg: #e9ebee;
    --card-bg: #ffffff;
    --brand-blue: #2f86ef;
    --brand-sky: #4fd3fa;
    --ink: #2b2d31;
    --ink-soft: #3a3c40;
  }
  * { margin: 0; padding: 0; box-sizing: border-box; }
  html, body {
    width: 1200px;
    height: 883px;
    overflow: hidden;
    background: var(--page-bg);
  }
  .card {
    position: absolute;
    left: 50px;
    top: 124px;
    width: 1100px;
    height: 635px;
    background: var(--card-bg);
    box-shadow: 0 6px 24px rgba(0, 0, 0, 0.12);
  }
  .brand {
    position: absolute;
    left: 0;
    right: 0;
    top: 170px;
    display: flex;
    align-items: center;
    justify-content: center;
    gap: 26px;
  }
  .brand-square {
    width: 60px;
    height: 60px;
    background: var(--brand-blue);
  }
  .brand-name {
    font-family: "Michroma", sans-serif;
    font-size: 46px;
    letter-spacing: 3px;
    color: var(--ink);
    line-height: 1;
  }
  .person {
    position: absolute;
    left: 46px;
    top: 468px;
  }
  .person-name {
    font-family: "Michroma", sans-serif;
    font-size: 35px;
    color: var(--brand-blue);
    line-height: 1.1;
  }
  .person-role {
    font-family: "Michroma", sans-serif;
    font-size: 25px;
    letter-spacing: 2px;
    color: var(--ink-soft);
    margin-top: 8px;
  }
  .contact {
    position: absolute;
    right: 42px;
    top: 462px;
    text-align: right;
    font-family: "Archivo", sans-serif;
    font-size: 31px;
    line-height: 40px;
    color: var(--ink);
    list-style: none;
  }
  .contact-label {
    color: var(--brand-blue);
    margin-right: 6px;
  }
</style>
</head>
<body>
  <main class="card">
    <div class="brand">
      <span class="brand-square"></span>
      <span class="brand-name">RK DECORATING</span>
    </div>

    <div class="person">
      <p class="person-name">Rob Kellaway</p>
      <p class="person-role">PAINTER</p>
    </div>

    <ul class="contact">
      <li>RK Decorating, LIC 581062B</li>
      <li><span class="contact-label">E</span>robert.kellaway@fernmail.net</li>
      <li><span class="contact-label">M</span>041 257 3068</li>
    </ul>
  </main>
</body>
</html>
```